Industry automation wholesale website

www.velqora.eu provides solutions for automation, building automation and digital signage.

Our products are rugged, reliable, energy saving and representative.

Scope of pages:
● welcome page
- scope of products
- applications, success stories and news
● category page
- short introduction
- sub categories
- product highlights
● product page
- short introduction
- about 3 to 4 pictures
- technical specifications: materials, dimensions
- price
- related products

Optional:
● contact page
- address
- contact form
● blog
- picture
- text
● logo
● favicon / apple touch icon

Conclusion:
● We need a professionally looking site
● Bright colors (e.g. white, grey, metalic colors, blue)

some pages we like:
http://www.brundafel.de/
http://www.korvimash.de/

Target Market(s)

Our target market is the industrial sector
● Target audience: engineering and IT professionals

Industry/Entity Type

Building

Requirements
Must have
• ● only use free available fonts e.g. Pellor Type Library (http://www.pellortype.com/webfonts)
Should not have
• ● sound
● flash

```html
<!DOCTYPE html>
<html lang="en">
<head>
<meta charset="utf-8">
<title>velqora – Industry automation</title>
<link rel="stylesheet" href="https://fonts.googleapis.com/css2?family=PT+Sans:wght@400;700&display=swap">
<style>
:root{
  --blue:#00aeef;
  --blue-light:#25c0f7;
  --blue-dark:#1689c2;
  --ink:#333333;
  --text:#555555;
  --muted:#8a8a8a;
  --white:#ffffff;
  --footer:#333333;
  --footer-side:#2a2a2a;
  --footer-base:#222222;
  --frame:#d0d0d0;
}
*{margin:0;padding:0;box-sizing:border-box}
html,body{width:1200px;height:1104px;overflow:hidden}
body{position:relative;background:var(--white);font-family:"PT Sans",Arial,sans-serif;color:var(--text)}
.abs{position:absolute}
.topbar{left:0;top:0;width:1200px;height:18px;background:var(--ink);color:#aaa;font-size:7px}
.topbar .lang{left:307px;top:5px}
.topbar .contact{top:2px;font-size:11px;color:#eee;display:flex;align-items:center;gap:8px}
.topbar .divider{left:798px;top:2px;width:1px;height:14px;background:#555}
.hero-band{left:0;top:18px;width:1200px;height:311px;background:var(--blue)}
.logo{left:307px;top:30px;font-size:40px;color:var(--white);letter-spacing:1px;display:flex;align-items:center;gap:10px}
.logo .dot{width:12px;height:12px;background:var(--white)}
.nav a{position:absolute;top:54px;font-size:11px;color:#1c3a4a;text-decoration:none}
.nav .active{color:var(--white);font-weight:700}
.nav .underline{left:522px;top:73px;width:42px;height:2px;background:var(--white)}
.cart{left:798px;top:18px;width:109px;height:57px;border-radius:0 0 4px 4px;overflow:hidden}
.cart .head{height:38px;background:var(--blue-dark);color:#e0f3fb;font-size:11px;display:flex;align-items:center;justify-content:center;gap:8px}
.cart .items{height:19px;background:var(--blue-light);color:var(--white);font-size:11px;text-align:center;line-height:19px}
.slider{left:307px;top:127px;width:600px;height:221px;background:var(--white);border-radius:4px}
.slider-shadow{left:490px;top:326px;width:310px;height:14px;border-radius:50%;box-shadow:0 8px 10px -4px rgba(0,0,0,.35)}
.slide-image{left:316px;top:137px;width:262px;height:179px;background:var(--ink)}
.dots{left:327px;top:300px;display:flex;gap:1px}
.dots span{width:7px;height:4px;background:var(--blue)}
.dots span.on{background:#6ad4fb}
.slide-panel{left:578px;top:137px;width:322px;height:179px;background:var(--blue-light);color:var(--white)}
.slide-panel h1{position:absolute;left:16px;top:20px;font-size:14px;font-weight:400}
.slide-panel .rule{position:absolute;left:16px;top:43px;width:290px;height:1px;background:rgba(255,255,255,.45)}
.slide-panel p{position:absolute;left:16px;top:60px;width:296px;font-size:9.4px;line-height:12px}
.slide-panel .more{position:absolute;right:35px;top:137px;font-size:7.5px;color:#1b7aa8}
.product h2,.section h2{font-size:10px;font-weight:400;color:var(--ink)}
.dotted{height:0;border-top:1px dotted #999}
.product{width:171px}
.product .dotted{margin-top:9px}
.product .img{margin-top:10px;height:73px;background:var(--ink)}
.product p{margin-top:11px;font-size:6px;line-height:9.5px;color:var(--text)}
.product .more{display:block;text-align:right;margin-top:12px;font-size:7.5px;color:var(--blue);padding-right:3px}
.about{left:307px;top:609px;width:271px}
.section .dotted{margin-top:6px}
.framed{border:1px solid var(--frame);padding:5px;background:var(--white)}
.framed div{width:100%;height:100%;background:var(--ink)}
.about .framed{left:307px;top:638px;width:106px;height:99px}
.body-text{font-size:7.3px;line-height:10px;color:var(--ink)}
.about .side{left:424px;top:642px;width:150px}
.about .side p+p{margin-top:10px}
.about .full{left:307px;top:746px;width:271px}
.link{color:var(--blue)}
.news{left:636px;top:609px;width:271px}
.news-item .framed{width:61px;height:58px;left:636px}
.news-item h3{position:absolute;left:713px;font-size:7.5px;font-weight:400;color:var(--blue)}
.news-item p{position:absolute;left:713px;width:190px}
.sep{left:636px;width:271px;height:1px;background:#e2e2e2}
.footer-line{left:0;top:924px;width:1200px;height:3px;background:var(--blue)}
.footer{left:0;top:927px;width:1200px;height:152px;background:var(--footer)}
.footer-side{left:708px;top:927px;width:492px;height:152px;background:var(--footer-side)}
.footer-col{top:953px;width:90px;color:#bbb}
.footer-col h4{font-size:10px;font-weight:400;color:#ccc}
.footer-col .dotted{width:53px;margin-top:6px;border-color:#999}
.footer-col ul{list-style:none;margin-top:7px;font-size:7.5px;line-height:10px}
.footer-cta{left:720px;top:953px;width:180px}
.footer-cta .call{font-size:10px;color:#ccc}
.footer-cta .phone{font-size:13px;color:var(--blue);margin-top:4px}
.footer-cta .flogo{margin-top:7px;font-size:22px;color:var(--blue);display:flex;align-items:center;gap:7px}
.footer-cta .flogo span.dot{width:8px;height:8px;background:var(--blue)}
.footer-cta .sub{margin-top:4px;font-size:7.5px;color:#bbb}
.newsletter{margin-top:6px;display:flex;height:25px}
.newsletter .email{width:118px;background:#4a4a4a;color:#aaa;font-size:7.5px;line-height:25px;padding-left:9px}
.newsletter .send{width:58px;background:var(--blue);color:var(--white);font-size:9px;font-weight:700;text-align:center;line-height:25px}
.base{left:0;top:1079px;width:1200px;height:25px;background:var(--footer-base);color:#999;font-size:6.5px}
.base span{position:absolute;left:307px;top:11px}
</style>
</head>
<body>
<header>
  <div class="abs topbar">
    <span class="abs lang">Language &nbsp; | EN | UK | &nbsp; IT</span>
    <span class="abs contact" style="left:690px">
      <svg width="13" height="13" viewBox="0 0 16 16"><circle cx="8" cy="8" r="7" fill="none" stroke="#eee" stroke-width="1.3"/><path d="M5.5 4.5l1.5 1.8-0.8 1c.6 1.2 1.4 2 2.6 2.6l1-.8 1.8 1.5-.9 1.2c-2.8-.3-5.3-2.8-5.6-5.6z" fill="#eee"/></svg>
      49-211-5547302</span>
    <span class="abs divider"></span>
    <span class="abs contact" style="left:816px">
      <svg width="14" height="11" viewBox="0 0 14 11"><rect x="0.5" y="0.5" width="13" height="10" fill="#eee"/><path d="M0.5 0.5l6.5 5.5 6.5-5.5" fill="none" stroke="#333" stroke-width="1"/></svg>
      info@velqora.de</span>
  </div>
  <div class="abs hero-band"></div>
  <div class="abs logo"><span>velqora</span><span class="dot"></span></div>
  <nav class="nav">
    <a class="active" href="#" style="left:531px">Home</a>
    <a href="#" style="left:593px">Products</a>
    <a href="#" style="left:669px">Contact</a>
    <span class="abs underline"></span>
  </nav>
  <div class="abs cart">
    <div class="head">Shopping cart
      <svg width="20" height="16" viewBox="0 0 20 16"><path d="M1 2h3l2.5 9h10l2-7H6" fill="none" stroke="#e0f3fb" stroke-width="1.8"/><circle cx="8" cy="14" r="1.5" fill="#e0f3fb"/><circle cx="15" cy="14" r="1.5" fill="#e0f3fb"/></svg>
    </div>
    <div class="items">Item (0)</div>
  </div>
</header>

<section>
  <div class="abs slider-shadow"></div>
  <div class="abs slider"></div>
  <div class="abs slide-image" role="img" aria-label="Featured automation product photo"></div>
  <div class="abs dots"><span></span><span class="on"></span><span></span><span></span><span></span></div>
  <div class="abs slide-panel">
    <h1>Lorem ipsum dolor sit amet</h1>
    <div class="rule"></div>
    <p>Lorem ipsum dolor sit amet, consectetur adipisicing elit, sed do eiusmod tempor incididunt ut labore et dolore magna aliqua. Ut enim ad minim veniam, quis nostrud exercitation ullamco laboris nisi ut aliquip ex ea commodo consequat.</p>
    <span class="more">Continue &gt;&gt;</span>
  </div>
</section>

<section>
  <article class="abs product" style="left:307px;top:383px">
    <h2>Modbus RTU / RS485 Remote IO Modules</h2>
    <div class="dotted"></div>
    <div class="img" role="img" aria-label="Remote IO module photo"></div>
    <p>RS485 Remote IO modules are ideal to realize decentralized distributed IO units over long distances. We provide the whole product range form Remote IO Modules with RS485</p>
    <span class="more">Continue &gt;&gt;</span>
  </article>
  <article class="abs product" style="left:522px;top:383px">
    <h2>Touch Panel Industry Computer</h2>
    <div class="dotted"></div>
    <div class="img" role="img" aria-label="Touch panel computer photo"></div>
    <p>RS485 Remote IO modules are ideal to realize decentralized distributed IO units over long distances. We provide the whole product range form Remote IO Modules with RS485</p>
    <span class="more">Continue &gt;&gt;</span>
  </article>
  <article class="abs product" style="left:735px;top:383px">
    <h2>Embedded systems for industrial automation</h2>
    <div class="dotted"></div>
    <div class="img" role="img" aria-label="Embedded system photo"></div>
    <p>RS485 Remote IO modules are ideal to realize decentralized distributed IO units over long distances. We provide the whole product range form Remote IO Modules with RS485</p>
    <span class="more">Continue &gt;&gt;</span>
  </article>
</section>

<section>
  <div class="abs section about"><h2>About</h2><div class="dotted"></div></div>
  <div class="abs framed" style="left:307px;top:638px;width:106px;height:99px"><div role="img" aria-label="Company photo"></div></div>
  <div class="abs body-text" style="left:424px;top:642px;width:150px">
    <p>Lorem ipsum dolor sit amet, consectetur adipisicing elit, sed do eiusmod tempor incididunt ut labore et dolore magna aliqua. laborum.</p>
    <p style="margin-top:10px">Lorem ipsum dolor sit amet, consectetur adipisicing elit, sed do <span class="link">eiusmod tempor</span> incididunt ut labore et dolore magna aliqua. laborum.</p>
  </div>
  <p class="abs body-text" style="left:307px;top:746px;width:271px">Lorem ipsum dolor sit amet, consectetur adipisicing elit, sed do eiusmod tempor incididunt ut labore et dolore magna aliqua. Ut enim ad minim veniam, quis nostrud exercitation ullamco laboris nisi ut aliquip ex ea commodo consequat. Duis aute irure dolor in reprehenderit in voluptate velit esse cillum dolore eu fugiat nulla pariatur. Excepteur sint occaecat cupidatat non proident, sunt in culpa qui officia deserunt mollit anim id est laborum.</p>

  <div class="abs section news"><h2>Latest News</h2><div class="dotted"></div></div>
  <div class="news-item">
    <div class="abs framed" style="left:636px;top:638px;width:61px;height:58px"><div role="img" aria-label="News photo"></div></div>
    <h3 style="top:638px">Lorem ipsum dolor sit amet</h3>
    <p class="body-text" style="top:660px">Lorem ipsum dolor sit amet, consectetur adipisicing elit, sed do eiusmod tempor incididunt ut labore et dolore magna aliqua.</p>
  </div>
  <div class="abs sep" style="top:708px"></div>
  <div class="news-item">
    <div class="abs framed" style="left:636px;top:721px;width:61px;height:58px"><div role="img" aria-label="News photo"></div></div>
    <h3 style="top:721px">Lorem ipsum dolor sit amet</h3>
    <p class="body-text" style="top:743px">Lorem ipsum dolor sit amet, consectetur adipisicing elit, sed do eiusmod tempor incididunt ut labore et dolore magna aliqua.</p>
  </div>
  <div class="abs sep" style="top:790px"></div>
  <div class="news-item">
    <div class="abs framed" style="left:636px;top:804px;width:61px;height:58px"><div role="img" aria-label="News photo"></div></div>
    <h3 style="top:804px">Lorem ipsum dolor sit amet</h3>
    <p class="body-text" style="top:826px">Lorem ipsum dolor sit amet, consectetur adipisicing elit, sed do eiusmod tempor incididunt ut labore et dolore magna aliqua.</p>
  </div>
  <div class="abs sep" style="top:873px"></div>
</section>

<footer>
  <div class="abs footer-line"></div>
  <div class="abs footer"></div>
  <div class="abs footer-side"></div>
  <div class="abs footer-col" style="left:308px"><h4>Lorem ipsum</h4><div class="dotted"></div><ul><li>Lorem ipsum</li><li>Lorem ipsum</li><li>Lorem ipsum</li><li>Lorem ipsum</li><li>Lorem ipsum</li><li>Lorem ipsum</li></ul></div>
  <div class="abs footer-col" style="left:406px"><h4>Lorem ipsum</h4><div class="dotted"></div><ul><li>Lorem ipsum</li><li>Lorem ipsum</li><li>Lorem ipsum</li><li>Lorem ipsum</li><li>Lorem ipsum</li><li>Lorem ipsum</li></ul></div>
  <div class="abs footer-col" style="left:511px"><h4>Lorem ipsum</h4><div class="dotted"></div><ul><li>Lorem ipsum</li><li>Lorem ipsum</li><li>Lorem ipsum</li><li>Lorem ipsum</li><li>Lorem ipsum</li><li>Lorem ipsum</li></ul></div>
  <div class="abs footer-col" style="left:624px"><h4>Lorem ipsum</h4><div class="dotted"></div><ul><li>Lorem ipsum</li><li>Lorem ipsum</li><li>Lorem ipsum</li><li>Lorem ipsum</li><li>Lorem ipsum</li><li>Lorem ipsum</li></ul></div>
  <div class="abs footer-cta">
    <div class="call">Rufen Sie uns an:</div>
    <div class="phone">+49 - 211 - 554 73 02</div>
    <div class="flogo"><span>velqora</span><span class="dot"></span></div>
    <div class="sub">Subscribe for Newsletters</div>
    <div class="newsletter"><span class="email">email@example.com</span><span class="send">Send</span></div>
  </div>
  <div class="abs base"><span>2014. Copyright. All Right Reserved.</span></div>
</footer>
</body>
</html>
```